Do i have coronavirus, flue or cold?

Using information from PFA and government agencies we want to make a easy to read infographic helping patients see if they have coronavirus, the flu or a cold. Using a flow diagram or whatever you think will make it easy to read and digest for the average lamen.

Information is in the word document and in the chart.

We are www.calvexa.co.uk attached is our brand guidelines, we will be putting this infographic on our website and email/sms it to all of our 300,000 patients.

```html
<!DOCTYPE html>
<html lang="en">
<head>
<meta charset="utf-8">
<title>Do I have coronavirus, the flu, or a cold?</title>
<link rel="stylesheet" href="https://fonts.googleapis.com/css2?family=Arimo:ital,wght@0,400;0,700;1,400&display=swap">
<style>
  :root {
    --navy: #3f4a9e;
    --periwinkle: #7889c6;
    --diamond-fill: #7589c6;
    --bg: #eef7f7;
    --header-text: #eef2fb;
    --result-fill: #f7a481;
    --result-stroke: #f0622a;
    --white: #ffffff;
  }
  html, body {
    margin: 0;
    padding: 0;
    width: 951px;
    height: 1200px;
    overflow: hidden;
    background: var(--bg);
  }
  .infographic {
    display: block;
    width: 951px;
    height: 1200px;
    font-family: "Arimo", Arial, sans-serif;
  }
  .header-band { fill: var(--navy); }
  .title { fill: var(--header-text); font-size: 29px; font-weight: 700; }
  .start-box { fill: none; stroke: var(--periwinkle); stroke-width: 3; }
  .start-label { fill: var(--periwinkle); font-size: 22px; text-anchor: middle; }
  .decision { fill: var(--diamond-fill); stroke: var(--navy); stroke-width: 3; }
  .decision-label { fill: var(--white); font-size: 22px; text-anchor: middle; }
  .connector { stroke: var(--periwinkle); stroke-width: 2; fill: none; }
  .arrowhead { fill: var(--periwinkle); }
  .branch-label { fill: var(--navy); font-size: 21px; font-style: italic; }
  .result-box { fill: var(--result-fill); stroke: var(--result-stroke); stroke-width: 3; }
  .result-label { fill: var(--white); font-size: 26px; font-weight: 700; text-anchor: middle; }
  .symptom-note { fill: var(--periwinkle); font-size: 21px; font-style: italic; }
</style>
</head>
<body>
<svg class="infographic" viewBox="0 0 951 1200" xmlns="http://www.w3.org/2000/svg">
  <rect width="951" height="1200" fill="var(--bg)"/>

  <!-- Header -->
  <rect class="header-band" x="0" y="0" width="951" height="87"/>
  <text class="title" x="82" y="55">Do I have coronavirus, the flu, or a cold?</text>

  <!-- Start -->
  <rect class="start-box" x="81" y="145" width="413" height="67"/>
  <text class="start-label" x="292" y="188">Start Self-diagnose</text>

  <line class="connector" x1="287" y1="212" x2="287" y2="300"/>
  <polygon class="arrowhead" points="280,291 294,291 287,317"/>

  <!-- Decision: fever / breath -->
  <polygon class="decision" points="287,317 494,409 287,500 80,409"/>
  <text class="decision-label" x="292" y="409">Having Fever/Experiencing</text>
  <text class="decision-label" x="292" y="438">Shortness of Breath</text>

  <!-- No → Cold -->
  <line class="connector" x1="494" y1="409" x2="628" y2="409"/>
  <polygon class="arrowhead" points="616,403 642,409 616,415"/>
  <text class="branch-label" x="549" y="397">No</text>

  <rect class="result-box" x="643" y="366" width="187" height="86"/>
  <text class="result-label" x="738" y="420">Cold</text>
  <text class="symptom-note" x="645" y="489">Other Typical Symptoms:</text>
  <text class="symptom-note" x="645" y="520">•Runny Nose</text>
  <text class="symptom-note" x="645" y="551">•Sneezing</text>

  <!-- Yes ↓ -->
  <line class="connector" x1="287" y1="500" x2="287" y2="632"/>
  <polygon class="arrowhead" points="280,622 294,622 287,647"/>
  <text class="branch-label" x="299" y="577">Yes</text>

  <!-- Decision: dry cough -->
  <polygon class="decision" points="287,647 494,726 287,804 80,726"/>
  <text class="decision-label" x="292" y="737">Having Dry Cough</text>

  <!-- No → Flu -->
  <line class="connector" x1="494" y1="726" x2="628" y2="726"/>
  <polygon class="arrowhead" points="616,720 642,726 616,732"/>
  <text class="branch-label" x="549" y="714">No</text>

  <rect class="result-box" x="643" y="683" width="187" height="87"/>
  <text class="result-label" x="737" y="737">Flu</text>
  <text class="symptom-note" x="645" y="814">Other Typical Symptoms:</text>
  <text class="symptom-note" x="645" y="844">•High fever</text>
  <text class="symptom-note" x="645" y="875">•Muscle Aches</text>

  <!-- Yes ↓ Coronavirus -->
  <line class="connector" x1="287" y1="804" x2="287" y2="950"/>
  <polygon class="arrowhead" points="280,940 294,940 287,965"/>
  <text class="branch-label" x="299" y="889">Yes</text>

  <rect class="result-box" x="193" y="965" width="188" height="87"/>
  <text class="result-label" x="289" y="1019">Coronavirus</text>
  <text class="symptom-note" x="191" y="1091">Other Typical Symptoms:</text>
  <text class="symptom-note" x="191" y="1122">•Tiredness</text>
</svg>
</body>
</html>
```